Kivo Commercial Cleaning is lookong for a new business card design.

A fresh new design that's professional and stylish. We need a serious upgrade to our business cards. I have included pictures of our existing ones. Our clients include professional individuals and business owners. We woupdblike something professional and upbeat. Please have fun and see what you come uo with.

Target Market(s)

Property managers, business owners, facility managers and other similar professionals

Industry/Entity Type

Janitorial

Contact Information for Business Card

Name, cell, office number, email, web address

Font styles to use
Sans Serif

Colors

Designer to choose colors to be used in the design.

Requirements
Must have
• please use the green color in our logo
Nice to have
• Bar code
Should not have
• Address

```html
<!DOCTYPE html>
<html lang="en">
<head>
<meta charset="utf-8">
<title>Kivo Commercial Cleaning – Business Card</title>
<link href="https://fonts.googleapis.com/css2?family=Montserrat:wght@400;500&family=Quicksand:wght@700&display=swap" rel="stylesheet">
<style>
  :root {
    --brand-green: #00b84f;
    --brand-blue: #0a6fae;
    --card-white: #ffffff;
    --ink: #333333;
    --backdrop: #3a3a3a;
  }
  * { margin: 0; padding: 0; box-sizing: border-box; }
  html, body { width: 1200px; height: 1200px; overflow: hidden; }
  body {
    background: var(--backdrop);
    display: flex;
    flex-direction: column;
    align-items: center;
    justify-content: center;
    gap: 60px;
  }
  .card {
    position: relative;
    width: 700px;
    height: 400px;
    border-radius: 26px;
    overflow: hidden;
  }
  .card-front { background: var(--card-white); }
  .card-back {
    background: var(--brand-green);
    display: flex;
    align-items: center;
    justify-content: center;
  }
  .contact-block {
    position: absolute;
    left: 64px;
    top: 150px;
    font-family: "Montserrat", sans-serif;
  }
  .person-name {
    color: var(--brand-green);
    font-weight: 500;
    font-size: 30px;
    letter-spacing: 0.5px;
    margin-bottom: 18px;
  }
  .contact-list { list-style: none; }
  .contact-item {
    display: flex;
    align-items: center;
    gap: 10px;
    color: var(--ink);
    font-size: 17px;
    line-height: 27px;
  }
  .contact-icon { width: 18px; height: 18px; flex: none; }
  .wordmark {
    font-family: "Quicksand", sans-serif;
    font-weight: 700;
    line-height: 1.05;
    text-align: center;
  }
  .wordmark-front {
    position: absolute;
    right: 60px;
    top: 90px;
    width: 270px;
    color: var(--brand-green);
    font-size: 34px;
  }
  .wordmark-back {
    color: var(--card-white);
    font-size: 56px;
  }
  .accent-bands {
    position: absolute;
    left: 0;
    bottom: 0;
    width: 700px;
    height: 60px;
  }
</style>
</head>
<body>
  <section class="card card-front">
    <div class="contact-block">
      <h1 class="person-name">DANA WHITFIELD</h1>
      <ul class="contact-list">
        <li class="contact-item">
          <svg class="contact-icon" viewBox="0 0 24 24"><path fill="var(--brand-green)" d="M6.6 10.8a15.1 15.1 0 0 0 6.6 6.6l2.2-2.2c.3-.3.7-.4 1-.2 1.1.4 2.3.6 3.6.6.6 0 1 .4 1 1V20c0 .6-.4 1-1 1A17 17 0 0 1 3 4c0-.6.4-1 1-1h3.5c.6 0 1 .4 1 1 0 1.3.2 2.5.6 3.6.1.3 0 .7-.2 1z"/></svg>
          (555) 014-2783
        </li>
        <li class="contact-item">
          <svg class="contact-icon" viewBox="0 0 24 24"><rect x="2" y="5" width="20" height="14" rx="1" fill="var(--brand-green)"/><path d="M2 6l10 7 10-7" fill="none" stroke="#fff" stroke-width="1.6"/></svg>
          dana@kivocleaning.com
        </li>
        <li class="contact-item">
          <svg class="contact-icon" viewBox="0 0 24 24" fill="none" stroke="var(--brand-green)" stroke-width="1.8"><circle cx="12" cy="12" r="9"/><path d="M3 12h18M12 3c3 3 3 15 0 18M12 3c-3 3-3 15 0 18"/></svg>
          www.kivocleaning.com
        </li>
      </ul>
    </div>
    <div class="wordmark wordmark-front">Kivo<br>Commercial Cleaning</div>
    <svg class="accent-bands" viewBox="0 0 700 60" preserveAspectRatio="none">
      <polygon points="0,48 404,48 396,60 0,60" fill="var(--brand-green)"/>
      <polygon points="414,30 700,30 700,60 404,60" fill="var(--brand-blue)"/>
    </svg>
  </section>

  <section class="card card-back">
    <div class="wordmark wordmark-back">Kivo<br>Commercial Cleaning</div>
  </section>
</body>
</html>
```